business card design for a small scale specialty cut flower farm

We need a business card design for Hollowmere Bloom Farm based in Langley, BC, Canada. We produce specialty, high-end cut flowers and sell locally to florists, local shops and markets and the end user through bouquet subscriptions. The final business card design should be memorable and have a timeless or vintage feel. We would prefer a square shape.
Updates

Target Market(s)

florists, shops and seasonal markets, local flower lovers

Industry/Entity Type

Floral

Contact Information for Business Card

Tamsin Ellery Voss, Grower
Langley, BC, Canada
website: hollowmerebloomfarm.example
instagram: @hollowmerebloomfarm
Tel: 555.317.4290
facebook: www.facebook.example/hollowmereblooms/

Font styles to use
Serif
Decorative
Script

Requirements
Must have
• soft black background colour on front side, the included logo and catch phrase: Fresh Local Seasonal
Nice to have
• phone number and website address on front of card, included photo 6539 incorporated onto the back, possibly photo 6609 as well.

```html
<!DOCTYPE html>
<html lang="en">
<head>
<meta charset="utf-8">
<title>Hollowmere Bloom Farm – Business Card</title>
<link rel="stylesheet" href="https://fonts.googleapis.com/css2?family=Josefin+Sans:wght@400&family=Sacramento&family=Dancing+Script:wght@600&family=Cormorant+SC:wght@500&family=Cormorant+Garamond:wght@500&display=swap">
<style>
  :root {
    --canvas-bg: #ebebea;
    --front-bg: #2b2828;
    --frame-green: #6f9a73;
    --ink-light: #f4efee;
    --ink-muted: #c9c1c0;
    --art-pink: #c98aa3;
    --art-pink-soft: #4a3a3f;
    --art-green: #5d7f5a;
    --back-bg: #c85a4e;
    --back-deep: #bb4c41;
    --back-light: #d27163;
    --back-art-pink: #e9aec4;
    --back-art-green: #6d9460;
    --white: #ffffff;
  }
  * { box-sizing: border-box; margin: 0; padding: 0; }
  html, body { width: 1200px; height: 1200px; overflow: hidden; }
  body { background: var(--canvas-bg); position: relative; }

  .card {
    position: absolute;
    top: 324px;
    width: 470px;
    height: 470px;
    overflow: hidden;
  }
  .card--front { left: 100px; background: var(--front-bg); }
  .card--back { left: 655px; background: var(--back-bg); color: var(--white); }

  .art { position: absolute; }

  .frame { position: absolute; pointer-events: none; }
  .card--front .frame { inset: 22px; border: 3px solid var(--frame-green); }
  .card--back .frame { inset: 27px; border: 2px solid var(--white); }

  /* Front artwork areas */
  .front-wash {
    background: linear-gradient(135deg, var(--art-pink-soft), rgba(74,58,63,0));
  }
  .front-wash--top-left { left: 0; top: 0; width: 200px; height: 150px; }
  .front-wash--bottom { left: 150px; top: 360px; width: 320px; height: 110px;
    background: linear-gradient(0deg, var(--art-pink-soft), rgba(74,58,63,0)); }
  .logo-bloom {
    left: 160px; top: 92px; width: 150px; height: 110px;
    border-radius: 10px;
    background: linear-gradient(135deg, var(--art-pink) 0%, var(--art-pink) 60%, var(--art-green) 100%);
  }

  .front-content {
    position: absolute;
    left: 0; right: 0; top: 232px;
    text-align: center;
    color: var(--ink-light);
  }
  .brand-name {
    font-family: "Josefin Sans", sans-serif;
    font-weight: 400;
    font-size: 30px;
    letter-spacing: 4px;
    text-transform: uppercase;
    line-height: 1.3;
  }
  .brand-tagline {
    font-family: "Sacramento", cursive;
    font-size: 25px;
    color: var(--ink-muted);
    margin-top: 8px;
  }
  .brand-est {
    font-family: "Josefin Sans", sans-serif;
    font-size: 11px;
    letter-spacing: 4px;
    color: var(--ink-muted);
    margin-top: 6px;
  }

  /* Back artwork areas */
  .back-shade--left { left: 40px; top: 50px; width: 200px; height: 200px;
    background: linear-gradient(160deg, var(--back-light), rgba(210,113,99,0)); }
  .back-shade--right { left: 280px; top: 140px; width: 170px; height: 200px;
    background: linear-gradient(200deg, var(--back-deep), rgba(187,76,65,0)); }
  .back-corner--top-right { right: 0; top: 0; width: 80px; height: 110px;
    background: linear-gradient(200deg, var(--back-art-pink), var(--back-art-pink) 70%, var(--back-art-green)); }
  .back-corner--top-left { left: 45px; top: 0; width: 95px; height: 26px;
    background: var(--back-art-green); }
  .back-corner--bottom-left { left: 0; top: 365px; width: 110px; height: 105px;
    background: linear-gradient(30deg, var(--back-art-green), var(--back-art-pink) 55%); }
  .back-corner--right { right: 0; top: 330px; width: 26px; height: 90px;
    background: var(--back-art-green); }

  .catchphrase {
    position: absolute;
    left: 0; right: 0; top: 84px;
    text-align: center;
    font-family: "Dancing Script", cursive;
    font-weight: 600;
    font-size: 34px;
    line-height: 48px;
  }
  .contact {
    position: absolute;
    left: 0; right: 0; top: 268px;
    text-align: center;
  }
  .contact__name {
    font-family: "Cormorant SC", serif;
    font-weight: 500;
    font-size: 25px;
    letter-spacing: 1px;
    line-height: 30px;
  }
  .contact__role {
    font-family: "Cormorant SC", serif;
    font-size: 16px;
    letter-spacing: 1px;
    line-height: 20px;
  }
  .contact__rule {
    width: 18px; height: 1.5px; background: var(--white);
    margin: 12px auto 9px;
  }
  .contact__web {
    font-family: "Cormorant SC", serif;
    font-size: 18px;
    letter-spacing: 0.5px;
    line-height: 22px;
  }
  .contact__phone {
    font-family: "Cormorant Garamond", serif;
    font-weight: 500;
    font-size: 19px;
    line-height: 24px;
  }
  .contact__social { margin-top: 5px; display: flex; justify-content: center; gap: 8px; }
  .social-dot { width: 11px; height: 11px; border-radius: 50%; background: var(--white); }
</style>
</head>
<body>

  <section class="card card--front" aria-label="Card front">
    <div class="art front-wash front-wash--top-left" role="img" aria-label="Watercolour petal wash"></div>
    <div class="art front-wash front-wash--bottom" role="img" aria-label="Watercolour petals along lower edge"></div>
    <div class="art logo-bloom" role="img" aria-label="Watercolour wild rose with leaves"></div>
    <div class="frame"></div>
    <div class="front-content">
      <h1 class="brand-name">Hollowmere<br>Bloom Farm</h1>
      <p class="brand-tagline">Specialty Cut Flowers</p>
      <p class="brand-est">EST. 2019</p>
    </div>
  </section>

  <section class="card card--back" aria-label="Card back">
    <div class="art back-shade--left" role="img" aria-label="Faint tonal watercolour petals"></div>
    <div class="art back-shade--right" role="img" aria-label="Faint tonal watercolour leaf"></div>
    <div class="art back-corner--top-left" role="img" aria-label="Watercolour leaves"></div>
    <div class="art back-corner--top-right" role="img" aria-label="Watercolour wild rose in corner"></div>
    <div class="art back-corner--right" role="img" aria-label="Watercolour leaf"></div>
    <div class="art back-corner--bottom-left" role="img" aria-label="Watercolour wild rose with leaves"></div>
    <div class="frame"></div>
    <p class="catchphrase">Fresh<br>Local<br>Seasonal</p>
    <div class="contact">
      <p class="contact__name">Tamsin Ellery Voss</p>
      <p class="contact__role">Owner</p>
      <div class="contact__rule"></div>
      <p class="contact__web">hollowmerebloomfarm.example</p>
      <p class="contact__phone">(555) 317-4290</p>
      <div class="contact__social">
        <span class="social-dot"></span>
        <span class="social-dot"></span>
      </div>
    </div>
  </section>

</body>
</html>
```